Website Home Page for Women's Health Medical Office

Redesign existing homepage for website using existing logo. Current website location is www.larkfieldwomenscare.com. Please give it a modern, streamlined, playful feel.

Please give it a feminine feel and make it bright and cheerful using logo colors.

Target Market(s)

Women between the ages of 25-45

Industry/Entity Type

Medical Office

Coding

Coded - Design and coding required

Number of Pages Required

1 page

Font styles to use
Sans Serif
Other font styles liked:
• SEGOI UI script for text and GIL SANS for bold (or their equivilent)

Colors
E54698
E96AAD
F1A4CE
F9D9EA
FCEFF6

Requirements
Must have
• Existing logo. Logo Colors. Feminine, cheerful, simple design. all relevant contact information
Nice to have
• clean lines and streamlined look
Should not have
• Cluttered

```html
<!DOCTYPE html>
<html lang="en">
<head>
<meta charset="utf-8">
<title>Larkfield OB/GYN — Better Health Start Here</title>
<link rel="stylesheet" href="https://fonts.googleapis.com/css2?family=Josefin+Sans:wght@400;600;700&family=Montserrat:wght@400;500;600;700&display=swap">
<style>
:root{
  --pink:#e5158a;
  --pink-2:#e54698;
  --pink-3:#e96aad;
  --pink-4:#f1a4ce;
  --pink-5:#f9d9ea;
  --pink-6:#fceff6;
  --ink:#222;
  --text:#444;
  --line:#cfcfcf;
  --dark:#2b2b2b;
}
*{margin:0;padding:0;box-sizing:border-box}
html,body{width:1200px;height:4228px;overflow:hidden;background:#fff}
body{font-family:"Montserrat",sans-serif;color:var(--text)}
.page{position:relative;width:1200px;height:4228px;overflow:hidden}
.abs{position:absolute}
.btn{position:absolute;display:flex;align-items:center;justify-content:center;border-radius:20px;background:var(--pink);color:#fff;font-size:13px;font-weight:500}
.heading{font-family:"Josefin Sans",sans-serif;color:var(--ink)}
.dots{position:absolute;height:4px;background:radial-gradient(circle,var(--pink-3) 1.2px,transparent 1.6px) 0 0/8px 4px}

/* header */
.brand{position:absolute;left:66px;top:0;width:197px;height:222px;background:#fff;clip-path:polygon(0 0,100% 0,100% 80%,50% 100%,0 80%);z-index:3}
.brand-mark{position:absolute;left:50%;top:42px;width:56px;height:56px;margin-left:-28px;border-radius:50%;background:var(--pink-5)}
.brand-name{position:absolute;left:0;right:0;top:118px;text-align:center;font-family:"Josefin Sans",sans-serif;font-weight:700;font-size:19px;color:var(--ink)}
.topbar{position:absolute;top:28px;display:flex;align-items:center;gap:10px;font-size:11.5px;line-height:14px;color:var(--ink);z-index:3}
.topbar small{display:block;color:var(--pink);font-size:10px}
.topbar .ico{width:26px;height:26px;border-radius:50%;background:#f2f2f2;display:flex;align-items:center;justify-content:center}
.nav{position:absolute;left:410px;top:89px;width:790px;height:51px;background:var(--pink);clip-path:polygon(40px 0,100% 0,100% 100%,0 100%);z-index:3}
.nav a{position:absolute;top:18px;color:#fff;text-decoration:none;font-family:"Josefin Sans",sans-serif;font-weight:600;font-size:13px;letter-spacing:.5px}

/* hero */
.hero-photo{position:absolute;left:0;top:0;width:1200px;height:812px;background:linear-gradient(90deg,#f3f3f3 0%,#ececec 30%,#dcdcdc 55%,#e8c4d8 78%,#f0e2d6 100%)}
.hero-title{position:absolute;left:72px;top:345px;font-family:"Josefin Sans",sans-serif;font-weight:600;font-size:56px;line-height:64px;color:var(--ink)}
.hero-title em{font-style:normal;color:var(--pink)}
.hero-text{position:absolute;left:72px;top:476px;width:290px;font-size:12.5px;line-height:22px;color:#333}

/* about */
.sec-title{position:absolute;left:0;right:0;text-align:center;font-family:"Josefin Sans",sans-serif;font-weight:600;color:var(--ink)}
.rule{position:absolute;height:3px;background:var(--pink);border-radius:2px}
.about-art{position:absolute;left:66px;top:952px;width:533px;height:345px;background:linear-gradient(180deg,#fff 0%,var(--pink-6) 40%,var(--pink-5) 50%,var(--pink-6) 60%,#fff 100%)}
.about-text{position:absolute;left:625px;top:960px;width:465px;font-size:12.5px;line-height:22px;color:#444}
.about-text p+p{margin-top:22px}
.about-text b{color:var(--ink)}

/* services */
.card{position:absolute;top:1523px;width:253px;height:384px;background:var(--pink-6);overflow:hidden}
.card .img{height:189px}
.card .icon{position:absolute;left:50%;top:160px;width:52px;height:52px;margin-left:-26px;border-radius:50%;background:#fff;display:flex;align-items:center;justify-content:center}
.card h3{position:absolute;top:216px;left:0;right:0;text-align:center;font-family:"Josefin Sans",sans-serif;font-weight:600;font-size:14px;color:var(--ink)}
.card .dots{left:107px;top:240px;width:40px}
.card p{position:absolute;top:256px;left:34px;right:34px;text-align:center;font-size:12.5px;line-height:22px;color:#444}
.card .corner{position:absolute;right:0;bottom:0;width:0;height:0;border-left:38px solid transparent;border-bottom:38px solid var(--pink)}
.card .plus{position:absolute;right:6px;bottom:4px;color:#fff;font-size:14px;font-weight:700}

/* insurance band */
.band{position:absolute;left:0;top:2095px;width:1200px;height:614px;background:linear-gradient(90deg,#ec3d9c,var(--pink) 60%,#e8339a)}
.band-photo{position:absolute;left:0;top:2095px;width:440px;height:614px;background:linear-gradient(135deg,#f4f4f4,#e6e6e6 50%,#cfcfcf);clip-path:polygon(0 0,100% 0,78% 100%,0 100%)}
.band-title{position:absolute;left:502px;top:2196px;font-family:"Josefin Sans",sans-serif;font-weight:600;font-size:34px;line-height:41px;color:#fff}
.plans{position:absolute;top:2310px;list-style:none;font-family:"Josefin Sans",sans-serif;font-weight:700;font-size:12px;line-height:22.5px;color:#fff}
.plans li{display:flex;gap:10px;align-items:flex-start}
.plans svg{flex:none;margin-top:4px}
.call{position:absolute;top:2561px;display:flex;align-items:center;gap:10px;color:#fff;font-size:12px}
.call .ico{width:36px;height:36px;border-radius:50%;background:var(--dark);display:flex;align-items:center;justify-content:center}
.call small{display:block;font-size:10px}

/* specialists */
.spec-text{position:absolute;left:112px;top:2930px;width:455px;font-size:12.5px;line-height:22px;color:#444}
.spec-text p+p{margin-top:22px}
.spec-photo{position:absolute;left:622px;top:2835px;width:463px;height:361px;border-radius:10px;background:linear-gradient(135deg,#f6f6f6,#efe3dc 55%,#e4cfc4)}

/* contact */
.field{position:absolute;height:45px;border:1px solid var(--line);border-radius:4px;font-size:13px;color:#555;padding:14px 12px}

/* footer */
.foot-bg{position:absolute;left:0;top:3740px;width:1200px;height:413px}
.foot-title{position:absolute;top:3898px;font-family:"Josefin Sans",sans-serif;font-weight:700;font-size:16px;color:var(--ink)}
.foot-links{position:absolute;left:366px;top:3950px;list-style:none;font-size:12.5px;line-height:24px;color:#444;letter-spacing:.5px}
.foot-item{position:absolute;left:602px;display:flex;gap:12px;font-size:13px;line-height:17px;color:#333}
.social{position:absolute;top:4170px;width:36px;height:36px;border-radius:50%}
</style>
</head>
<body>
<div class="page">

  <!-- Hero -->
  <div class="hero-photo" role="img" aria-label="Smiling doctor examining a pregnant patient resting on a pink blanket"></div>
  <svg class="abs" style="left:0;top:700px" width="1200" height="130" viewBox="0 0 1200 130">
    <path d="M0 110 C 300 140, 500 60, 760 70 C 960 78, 1080 120, 1200 50 L1200 130 L0 130Z" fill="#fff"/>
    <path d="M520 92 C 700 40, 900 60, 1020 95 C 1100 115, 1160 80, 1200 42" fill="none" stroke="var(--pink)" stroke-width="10"/>
  </svg>

  <div class="brand">
    <div class="brand-mark"></div>
    <div class="brand-name">Larkfield OB/GYN</div>
  </div>

  <div class="topbar" style="left:548px">
    <span class="ico"><svg width="12" height="12" viewBox="0 0 24 24"><path fill="var(--pink)" d="M6.6 10.8a15 15 0 0 0 6.6 6.6l2.2-2.2c.3-.3.7-.4 1-.2 1.1.4 2.3.6 3.6.6.6 0 1 .4 1 1V20c0 .6-.4 1-1 1A17 17 0 0 1 3 4c0-.6.4-1 1-1h3.5c.6 0 1 .4 1 1 0 1.2.2 2.4.6 3.6.1.3 0 .7-.2 1z"/></svg></span>
    <div><small>Call Us</small>(555) 014-2280</div>
  </div>
  <div class="topbar" style="left:682px">
    <span class="ico"><svg width="12" height="12" viewBox="0 0 24 24"><path fill="var(--pink)" d="M3 5h18v14H3z"/><path d="M3 6l9 7 9-7" fill="none" stroke="#fff" stroke-width="2"/></svg></span>
    <div><small>Email us</small>admin@larkfieldwomenscare.com</div>
  </div>
  <div class="btn" style="left:927px;top:26px;width:196px;height:38px;font-weight:600;z-index:3">Make An Appointment</div>

  <nav class="nav">
    <a style="left:99px">Home</a>
    <a style="left:179px">About us</a>
    <a style="left:303px">Services ⌄</a>
    <a style="left:420px">Resource</a>
    <a style="left:542px">News</a>
    <a style="left:637px">Contact us</a>
  </nav>

  <h1 class="hero-title"><em>Better</em> Health<br>Start <em>Here</em></h1>
  <p class="hero-text">Lorem Ipsum is simply dummy text of the printing and typesetting industry.</p>
  <div class="btn" style="left:74px;top:532px;width:128px;height:38px">Read More</div>
  <svg class="abs" style="left:70px;top:706px" width="70" height="16">
    <circle cx="6" cy="8" r="2.5" fill="var(--ink)"/><circle cx="27" cy="8" r="5" fill="var(--pink)"/>
    <circle cx="46" cy="8" r="2.5" fill="var(--ink)"/><circle cx="62" cy="8" r="2.5" fill="var(--ink)"/>
  </svg>

  <!-- About -->
  <h2 class="sec-title" style="top:875px;font-size:33px">About us</h2>
  <div class="rule" style="left:565px;top:927px;width:68px"></div>
  <div class="about-art" role="img" aria-label="Line illustration of a doctor with a clipboard consulting a seated patient"></div>
  <div class="about-text">
    <p><b>Larkfield OB/GYN in Larkfield</b>, California, was formed in October of 2005 by Dr. Peter Holm and Dr. Clara Venn. to help service the greats need for women's health services in the Southwest Valley region. In October of 2012, Dr. Holm retired, and Dr. Nora Pike joined the practice. In December of 2015, Dr. Pike left the practice, leaving Dr. Venn to carry on as a solo practitioner. In November of 2022, Dr. Iris Dalton joined the Larkfield OB/GYN family.</p>
    <p>Larkfield OB/GYN is a provider for Larkfield Valley Medical Center and has privileges at Oakridge Medical Center. Currently, there are two medical doctors, Dr. Clara Venn and Dr. Iris Dalton, and one physician's assistant, Mia Ford, PA-C, serving the needs of its patients.</p>
  </div>
  <div class="btn" style="left:622px;top:1267px;width:153px;height:40px">Read More</div>

  <!-- Services -->
  <h2 class="sec-title" style="top:1432px;font-size:33px">Services</h2>
  <div class="sec-title" style="top:1474px;font-family:Montserrat,sans-serif;font-weight:400;font-size:12px;letter-spacing:1.5px;color:#333">HOW CAN WE HELP YOU?</div>

  <div class="card" style="left:74px">
    <div class="img" role="img" aria-label="Doctor caring for a pregnant patient" style="background:linear-gradient(135deg,#eee,#e7c9d8)"></div>
    <div class="icon"><svg width="28" height="28" viewBox="0 0 24 24"><path d="M12 20s-8-5-8-11a4 4 0 0 1 8-1 4 4 0 0 1 8 1c0 6-8 11-8 11z" fill="none" stroke="var(--pink)" stroke-width="1.6"/></svg></div>
    <h3>PREGNANCY CARE</h3><div class="dots"></div>
    <p>Receiving regular care in pregnancy is important for the health of both you and your baby...</p>
    <div class="corner"></div><span class="plus">+</span>
  </div>
  <div class="card" style="left:338px">
    <div class="img" role="img" aria-label="Gynecologist talking with a patient in an office" style="background:linear-gradient(135deg,#f2f2f2,#d9d9d9)"></div>
    <div class="icon"><svg width="28" height="28" viewBox="0 0 24 24"><circle cx="12" cy="9" r="6" fill="none" stroke="var(--pink)" stroke-width="1.6"/><path d="M12 15v6M9 18h6" stroke="var(--pink)" stroke-width="1.6"/></svg></div>
    <h3>BIRTH CONTROL</h3><div class="dots"></div>
    <p>Our gynecologists are knowledgeable on all forms of birth control including the IUD, the implant...</p>
    <div class="corner"></div><span class="plus">+</span>
  </div>
  <div class="card" style="left:604px">
    <div class="img" role="img" aria-label="Nurse measuring a patient's blood pressure" style="background:linear-gradient(135deg,#f4f4f4,#dcdcdc)"></div>
    <div class="icon"><svg width="28" height="28" viewBox="0 0 24 24"><circle cx="12" cy="7" r="4" fill="none" stroke="var(--pink)" stroke-width="1.6"/><path d="M4 21c0-5 4-7 8-7s8 2 8 7" fill="none" stroke="var(--pink)" stroke-width="1.6"/></svg></div>
    <h3>WELL WOMAN EXAMS</h3><div class="dots"></div>
    <p>Our providers will help you to stay healthy by performing a physical exam on you annually...</p>
    <div class="corner"></div><span class="plus">+</span>
  </div>
  <div class="card" style="left:870px">
    <div class="img" role="img" aria-label="Woman seated on the floor with abdominal pain" style="background:linear-gradient(135deg,#eeeeee,#cdd6e0)"></div>
    <div class="icon"><svg width="28" height="28" viewBox="0 0 24 24"><circle cx="12" cy="6" r="3" fill="none" stroke="var(--pink)" stroke-width="1.6"/><path d="M5 10l4 2v9M19 10l-4 2v9M9 16h6" fill="none" stroke="var(--pink)" stroke-width="1.6"/></svg></div>
    <h3>WOMEN'S HEALTH</h3><div class="dots"></div>
    <p>Whether you are dealing with painful or irregular periods, fibroids, or other women's health issues...</p>
    <div class="corner"></div><span class="plus">+</span>
  </div>
  <div class="btn" style="left:522px;top:1940px;width:153px;height:40px">View More</div>

  <!-- Insurance band -->
  <div class="band"></div>
  <div class="band-photo" role="img" aria-label="Doctor in a white coat holding a stethoscope"></div>
  <h2 class="band-title">Personalized<br>Medical Care For Women</h2>
  <div class="dots" style="left:505px;top:2288px;width:40px;background:radial-gradient(circle,#fff 1.2px,transparent 1.6px) 0 0/8px 4px"></div>

  <ul class="plans" style="left:506px">
    <li><svg width="12" height="12" viewBox="0 0 12 12"><circle cx="6" cy="6" r="5" fill="none" stroke="#fff"/><path d="M3.5 6l2 2 3-4" fill="none" stroke="#fff" stroke-width="1.3"/></svg>Meadow Health Plan</li>
    <li><svg width="12" height="12" viewBox="0 0 12 12"><circle cx="6" cy="6" r="5" fill="none" stroke="#fff"/><path d="M3.5 6l2 2 3-4" fill="none" stroke="#fff" stroke-width="1.3"/></svg>Bayline Direct</li>
    <li><svg width="12" height="12" viewBox="0 0 12 12"><circle cx="6" cy="6" r="5" fill="none" stroke="#fff"/><path d="M3.5 6l2 2 3-4" fill="none" stroke="#fff" stroke-width="1.3"/></svg>Crestview Care North</li>
    <li><svg width="12" height="12" viewBox="0 0 12 12"><circle cx="6" cy="6" r="5" fill="none" stroke="#fff"/><path d="M3.5 6l2 2 3-4" fill="none" stroke="#fff" stroke-width="1.3"/></svg>Crestview Care East</li>
    <li><svg width="12" height="12" viewBox="0 0 12 12"><circle cx="6" cy="6" r="5" fill="none" stroke="#fff"/><path d="M3.5 6l2 2 3-4" fill="none" stroke="#fff" stroke-width="1.3"/></svg>Summit Senior Plan</li>
    <li><svg width="12" height="12" viewBox="0 0 12 12"><circle cx="6" cy="6" r="5" fill="none" stroke="#fff"/><path d="M3.5 6l2 2 3-4" fill="none" stroke="#fff" stroke-width="1.3"/></svg>Harbor Medical Group</li>
    <li><svg width="12" height="12" viewBox="0 0 12 12"><circle cx="6" cy="6" r="5" fill="none" stroke="#fff"/><path d="M3.5 6l2 2 3-4" fill="none" stroke="#fff" stroke-width="1.3"/></svg>Northstar Prime</li>
    <li><svg width="12" height="12" viewBox="0 0 12 12"><circle cx="6" cy="6" r="5" fill="none" stroke="#fff"/><path d="M3.5 6l2 2 3-4" fill="none" stroke="#fff" stroke-width="1.3"/></svg>Valley Partners</li>
    <li><svg width="12" height="12" viewBox="0 0 12 12"><circle cx="6" cy="6" r="5" fill="none" stroke="#fff"/><path d="M3.5 6l2 2 3-4" fill="none" stroke="#fff" stroke-width="1.3"/></svg>Fernwood Open Access</li>
    <li><svg width="12" height="12" viewBox="0 0 12 12"><circle cx="6" cy="6" r="5" fill="none" stroke="#fff"/><path d="M3.5 6l2 2 3-4" fill="none" stroke="#fff" stroke-width="1.3"/></svg></li>
  </ul>
  <ul class="plans" style="left:747px">
    <li><svg width="12" height="12" viewBox="0 0 12 12"><circle cx="6" cy="6" r="5" fill="none" stroke="#fff"/><path d="M3.5 6l2 2 3-4" fill="none" stroke="#fff" stroke-width="1.3"/></svg>Aster Select</li>
    <li><svg width="12" height="12" viewBox="0 0 12 12"><circle cx="6" cy="6" r="5" fill="none" stroke="#fff"/><path d="M3.5 6l2 2 3-4" fill="none" stroke="#fff" stroke-width="1.3"/></svg>Bluebell Shield</li>
    <li><svg width="12" height="12" viewBox="0 0 12 12"><circle cx="6" cy="6" r="5" fill="none" stroke="#fff"/><path d="M3.5 6l2 2 3-4" fill="none" stroke="#fff" stroke-width="1.3"/></svg>Corvid Health</li>
    <li><svg width="12" height="12" viewBox="0 0 12 12"><circle cx="6" cy="6" r="5" fill="none" stroke="#fff"/><path d="M3.5 6l2 2 3-4" fill="none" stroke="#fff" stroke-width="1.3"/></svg>Corvid Local Plus</li>
    <li><svg width="12" height="12" viewBox="0 0 12 12"><circle cx="6" cy="6" r="5" fill="none" stroke="#fff"/><path d="M3.5 6l2 2 3-4" fill="none" stroke="#fff" stroke-width="1.3"/></svg>Veterans Plan A</li>
    <li><svg width="12" height="12" viewBox="0 0 12 12"><circle cx="6" cy="6" r="5" fill="none" stroke="#fff"/><path d="M3.5 6l2 2 3-4" fill="none" stroke="#fff" stroke-width="1.3"/></svg>EBS Health</li>
    <li><svg width="12" height="12" viewBox="0 0 12 12"><circle cx="6" cy="6" r="5" fill="none" stroke="#fff"/><path d="M3.5 6l2 2 3-4" fill="none" stroke="#fff" stroke-width="1.3"/></svg>Federal Care Plan</li>
    <li><svg width="12" height="12" viewBox="0 0 12 12"><circle cx="6" cy="6" r="5" fill="none" stroke="#fff"/><path d="M3.5 6l2 2 3-4" fill="none" stroke="#fff" stroke-width="1.3"/></svg>Wellnest</li>
    <li><svg width="12" height="12" viewBox="0 0 12 12"><circle cx="6" cy="6" r="5" fill="none" stroke="#fff"/><path d="M3.5 6l2 2 3-4" fill="none" stroke="#fff" stroke-width="1.3"/></svg>Humble Health</li>
    <li><svg width="12" height="12" viewBox="0 0 12 12"><circle cx="6" cy="6" r="5" fill="none" stroke="#fff"/><path d="M3.5 6l2 2 3-4" fill="none" stroke="#fff" stroke-width="1.3"/></svg>Iron Trades Trust Fund</li>
  </ul>
  <ul class="plans" style="left:962px">
    <li><svg width="12" height="12" viewBox="0 0 12 12"><circle cx="6" cy="6" r="5" fill="none" stroke="#fff"/><path d="M3.5 6l2 2 3-4" fill="none" stroke="#fff" stroke-width="1.3"/></svg>Builders Health &amp;<br>Welfare Fund</li>
    <li><svg width="12" height="12" viewBox="0 0 12 12"><circle cx="6" cy="6" r="5" fill="none" stroke="#fff"/><path d="M3.5 6l2 2 3-4" fill="none" stroke="#fff" stroke-width="1.3"/></svg>Postal Carriers Plan</li>
    <li><svg width="12" height="12" viewBox="0 0 12 12"><circle cx="6" cy="6" r="5" fill="none" stroke="#fff"/><path d="M3.5 6l2 2 3-4" fill="none" stroke="#fff" stroke-width="1.3"/></svg>Engineers Benefit Trust</li>
    <li><svg width="12" height="12" viewBox="0 0 12 12"><circle cx="6" cy="6" r="5" fill="none" stroke="#fff"/><path d="M3.5 6l2 2 3-4" fill="none" stroke="#fff" stroke-width="1.3"/></svg>Metal Trades Workers</li>
    <li><svg width="12" height="12" viewBox="0 0 12 12"><circle cx="6" cy="6" r="5" fill="none" stroke="#fff"/><path d="M3.5 6l2 2 3-4" fill="none" stroke="#fff" stroke-width="1.3"/></svg>Northstar Select</li>
    <li><svg width="12" height="12" viewBox="0 0 12 12"><circle cx="6" cy="6" r="5" fill="none" stroke="#fff"/><path d="M3.5 6l2 2 3-4" fill="none" stroke="#fff" stroke-width="1.3"/></svg>UnityCare</li>
    <li><svg width="12" height="12" viewBox="0 0 12 12"><circle cx="6" cy="6" r="5" fill="none" stroke="#fff"/><path d="M3.5 6l2 2 3-4" fill="none" stroke="#fff" stroke-width="1.3"/></svg>Grocers Union Plan</li>
    <li><svg width="12" height="12" viewBox="0 0 12 12"><circle cx="6" cy="6" r="5" fill="none" stroke="#fff"/><path d="M3.5 6l2 2 3-4" fill="none" stroke="#fff" stroke-width="1.3"/></svg>Meridian Benefits</li>
    <li><svg width="12" height="12" viewBox="0 0 12 12"><circle cx="6" cy="6" r="5" fill="none" stroke="#fff"/><path d="M3.5 6l2 2 3-4" fill="none" stroke="#fff" stroke-width="1.3"/></svg>Crestview Care West</li>
  </ul>

  <div class="btn" style="left:501px;top:2561px;width:195px;height:36px;background:var(--dark);font-weight:600">Make An Appointment</div>
  <div class="call" style="left:708px">
    <span class="ico"><svg width="14" height="14" viewBox="0 0 24 24"><path fill="#fff" d="M6.6 10.8a15 15 0 0 0 6.6 6.6l2.2-2.2c.3-.3.7-.4 1-.2 1.1.4 2.3.6 3.6.6.6 0 1 .4 1 1V20c0 .6-.4 1-1 1A17 17 0 0 1 3 4c0-.6.4-1 1-1h3.5c.6 0 1 .4 1 1 0 1.2.2 2.4.6 3.6.1.3 0 .7-.2 1z"/></svg></span>
    <div><small>Call Us</small>(555) 014-2280</div>
  </div>

  <!-- Specialists -->
  <h2 class="heading abs" style="left:112px;top:2860px;font-size:34px;font-weight:700">YOUR OB/GYN SPECIALISTS</h2>
  <div class="dots" style="left:112px;top:2912px;width:32px"></div>
  <div class="spec-text">
    <p>Larkfield OB/GYN offers you the best care possible in a personalized setting. We are currently accepting patients. Call our office now to make an appointment.</p>
    <p>Larkfield OB/GYN (located near Larkfield Valley Hospital in Larkfield, CA) is a medical office that specializes in Christ-centered healthcare for women of all ages. Our team of exclusively female providers have years of experience taking care of women with a variety of pregnancy and gynecology concerns.</p>
  </div>
  <div class="btn" style="left:113px;top:3152px;width:155px;height:38px">Read More</div>
  <div class="spec-photo" role="img" aria-label="Newborn baby held in a parent's hands"></div>

  <!-- Quick contact -->
  <h2 class="sec-title" style="top:3298px;font-size:34px;font-weight:700">QUICK CONTACT</h2>
  <div class="field" style="left:254px;top:3360px;width:223px">Name*</div>
  <div class="field" style="left:489px;top:3360px;width:223px">Phone*</div>
  <div class="field" style="left:724px;top:3360px;width:223px">Email*</div>
  <div class="field" style="left:254px;top:3421px;width:693px;height:43px;padding-top:13px">Type of request<span style="position:absolute;right:14px;top:12px">⌄</span></div>
  <div class="field" style="left:254px;top:3482px;width:693px;height:131px">Message</div>
  <div class="btn" style="left:522px;top:3631px;width:154px;height:40px">Submit</div>

  <!-- Footer -->
  <svg class="foot-bg" viewBox="0 0 1200 413" preserveAspectRatio="none">
    <path d="M0 40 C 250 0, 450 60, 700 45 C 900 32, 1050 0, 1200 20 L1200 413 L0 413Z" fill="var(--pink-6)"/>
  </svg>
  <div class="abs" style="left:74px;top:3915px;width:189px;height:164px">
    <div style="position:absolute;left:66px;top:8px;width:56px;height:56px;border-radius:50%;background:var(--pink-5)"></div>
    <div style="position:absolute;left:0;right:0;top:88px;text-align:center;font-family:'Josefin Sans',sans-serif;font-weight:700;font-size:19px;color:var(--ink)">Larkfield OB/GYN</div>
  </div>

  <div class="foot-title" style="left:366px">QUICK LINKS</div>
  <ul class="foot-links">
    <li>· <b style="color:var(--ink);font-weight:600">Home</b></li>
    <li>· About us</li>
    <li>· Services</li>
    <li>· Resource</li>
    <li>· News</li>
    <li>· Contact us</li>
  </ul>

  <div class="foot-title" style="left:602px">CONTACT DETAIL</div>
  <div class="foot-item" style="top:3958px">
    <svg width="12" height="30" viewBox="0 0 12 30"><path fill="var(--pink)" d="M3 2h2l1 3-1.5 1a7 7 0 0 0 3 3L9 7.5l3 1v2c0 .5-.5 1-1 1A10 10 0 0 1 2 3c0-.5.5-1 1-1z"/><path fill="var(--pink)" d="M3 17h2l1 3-1.5 1a7 7 0 0 0 3 3L9 22.5l3 1v2c0 .5-.5 1-1 1A10 10 0 0 1 2 18c0-.5.5-1 1-1z"/></svg>
    <div>(555) 014-2280<br>(555) 014-2291</div>
  </div>
  <div class="foot-item" style="top:4003px">
    <svg width="12" height="12" viewBox="0 0 24 24"><path fill="var(--pink)" d="M2 5h20v14H2z"/><path d="M2 6l10 7 10-7" fill="none" stroke="#fff" stroke-width="2"/></svg>
    <div>admin@larkfieldwomenscare.com</div>
  </div>
  <div class="foot-item" style="top:4048px">
    <svg width="12" height="14" viewBox="0 0 24 28"><path fill="var(--pink)" d="M12 0a9 9 0 0 0-9 9c0 7 9 17 9 17s9-10 9-17a9 9 0 0 0-9-9zm0 12a3 3 0 1 1 0-6 3 3 0 0 1 0 6z"/></svg>
    <div>1840 Orchard Lane,<br>Suite 210, Larkfield, CA 90871</div>
  </div>

  <div class="foot-title" style="left:878px">NEWSLETTER</div>
  <p class="abs" style="left:878px;top:3950px;width:250px;font-size:12.5px;line-height:22px;color:#444">Lorem Ipsum is simply dummy text of printing and typesetting industry.</p>
  <div class="abs" style="left:878px;top:4004px;width:245px;height:36px;border-radius:18px;background:#fff;border:1px solid #eee;font-size:11px;font-style:italic;color:#666;padding:11px 18px">Email Address</div>
  <div class="btn" style="left:878px;top:4050px;width:153px;height:36px;font-size:12px;font-weight:600">SUBSCRIBE</div>

  <div class="abs" style="left:0;top:4153px;width:1200px;height:75px;background:#fff"></div>
  <p class="abs" style="left:74px;top:4182px;font-size:12.5px;color:#333">Copyright © 2022 <b>Larkfield OB/GYN</b>, All Rights Reserved.</p>
  <span class="social" style="left:946px;background:var(--pink)"></span>
  <span class="social" style="left:993px;background:var(--dark)"></span>
  <span class="social" style="left:1041px;background:var(--dark)"></span>
  <span class="social" style="left:1088px;background:var(--dark)"></span>

</div>
</body>
</html>
```